Small Business coaching and services company

Need a powerpoint template design for a company that provides Human Resources services as well sales and business coaching.

```html
<!DOCTYPE html>
<html lang="en">
<head>
<meta charset="utf-8">
<title>BrightPath – HR &amp; Business Coaching Presentation Template</title>
<link href="https://fonts.googleapis.com/css2?family=Titillium+Web:wght@400;600;700&display=swap" rel="stylesheet">
<style>
:root{
  --purple:#66379b;
  --purple-soft:#a597bb;
  --orange:#f5a623;
  --teal:#17a196;
  --pink:#ef5a7a;
  --blue:#3a5cc4;
  --pale:#f1e6b8;
  --ink:#2b2b33;
  --grey:#8a8a94;
  --panel:#f0f0f3;
  --page:#ffffff;
}
*{box-sizing:border-box;margin:0;padding:0}
html,body{width:1200px;height:1200px;overflow:hidden;background:var(--page)}
body{font-family:"Titillium Web",sans-serif;color:var(--ink)}
.deck{position:absolute;left:80px;top:32px;display:grid;grid-template-columns:repeat(4,210px);grid-auto-rows:118px;column-gap:67px;row-gap:10px}
.slide{position:relative;width:210px;height:118px;background:#fff;overflow:hidden;box-shadow:0 3px 10px rgba(0,0,0,.28)}
.slide > *{position:absolute}
.brand{display:flex;align-items:center;gap:1.5px;font-weight:700;font-size:5.2px;color:var(--purple);top:9px;right:14px;letter-spacing:.1px}
.brand i{display:block;width:5px;height:5px;border-radius:50%;background:var(--purple)}
.brand.left{right:auto;left:14px}
.brand.light{color:#fff}.brand.light i{background:#fff}
.foot{left:17px;right:17px;bottom:3px;display:flex;justify-content:space-between;font-size:1.9px;color:var(--grey)}
.kicker{font-size:2.2px;color:var(--purple);margin-bottom:2px}
h2{font-size:6.4px;font-weight:400;line-height:1.3;color:var(--ink)}
h2 b{font-weight:600;color:var(--purple)}
.light h2,.light .copy,.light .kicker{color:#fff}
.light h2 b{color:#fff}
.sub{font-size:2.3px;font-weight:700;margin-top:3px}
.copy{font-size:1.9px;line-height:1.55;color:var(--grey);margin-top:3px}
.btn{display:inline-block;margin-top:4px;background:var(--purple);color:#fff;font-size:1.6px;padding:1px 3px}
.btn.orange{background:var(--orange)}
.photo{background:linear-gradient(135deg,#d9d6de,#8b8594 60%,#4a4552)}
.photo.warm{background:linear-gradient(135deg,#d8c4ae,#8c6f58 55%,#3c3028)}
.photo.desk{background:linear-gradient(135deg,#f4f4f4,#cfcfcf 60%,#3a3a3a)}
.photo.crowd{background:linear-gradient(160deg,#e0e0e0,#7b7b7b 50%,#2a2a2a)}
.photo.violet{background:linear-gradient(120deg,#8a6bb3,#5b3b8c 60%,#3b2663)}
.panel{background:var(--panel)}
.card{background:#fff;box-shadow:0 1px 3px rgba(0,0,0,.25);padding:3px;font-size:1.8px;color:var(--grey)}
.card strong{display:block;font-size:2.2px;color:var(--ink);margin-bottom:1px}
.cap{font-size:1.9px;color:var(--grey);line-height:1.5}
.cap strong{color:var(--purple)}
.hd{left:17px;top:10px;font-size:6.4px;color:var(--ink)}
.hd b{color:var(--purple);font-weight:600}
svg text{font-family:"Titillium Web",sans-serif}
.lbl{font-size:2px;color:var(--grey);line-height:1.4;text-align:center}
.lbl strong{display:block;color:var(--ink);font-size:2.2px}
table{border-collapse:collapse;font-size:1.8px;color:var(--ink)}
th{background:var(--purple);color:#fff;font-weight:400;padding:1.3px 3px;text-align:left}
td{padding:1.6px 3px;border-bottom:.3px solid #ddd}
td:first-child{color:var(--grey)}
tr:nth-child(even) td{background:#f6f5f8}
</style>
</head>
<body>
<main class="deck">

<!-- 1 cover -->
<section class="slide">
  <div class="photo" style="left:0;top:0;width:110px;height:118px;background:radial-gradient(circle at 45% 55%,#7b5aa8 0 30%,#b9acd0 45%,#e8e6ec 70%)" role="img" aria-label="Team of professionals framed by a curved growth arrow"></div>
  <div class="brand" style="right:27px;top:35px">BrightPath</div>
  <h2 style="left:112px;top:48px;width:90px;text-align:center">YOUR PRESENTATION<br><span style="font-weight:600">TITLE GOES HERE</span></h2>
  <p class="copy" style="left:117px;top:66px;width:80px;text-align:center;color:var(--ink);font-size:2.8px">BrightPath Human Resources services &amp; business coaching.</p>
  <div class="foot"><span></span><span>Human Resources services &amp; business coaching &nbsp; BrightPath | 1</span></div>
</section>

<!-- 2 cover alt -->
<section class="slide light" style="background:var(--purple-soft)">
  <div class="photo violet" style="left:0;top:0;width:112px;height:118px;opacity:.75" role="img" aria-label="Crowd of people seen from above inside a growth arrow shape"></div>
  <div class="brand light" style="right:24px;top:34px">BrightPath</div>
  <h2 style="left:112px;top:48px;width:92px;text-align:center">YOUR PRESENTATION<br>TITLE GOES HERE</h2>
  <p class="copy" style="left:118px;top:66px;width:80px;text-align:center;font-size:2.8px">BrightPath Human Resources services &amp; business coaching.</p>
  <div class="foot" style="color:#e6e0ee"><span></span><span>Human Resources services &amp; business coaching</span></div>
</section>

<!-- 3 -->
<section class="slide">
  <div class="panel" style="left:0;top:0;width:210px;height:97px"></div>
  <div class="brand">BrightPath</div>
  <div style="left:19px;top:27px;width:70px"><p class="kicker">Human Resources services</p><h2>YOUR SLIDE<br><b>TITLE GOES HERE</b></h2><p class="copy">Lorem ipsum is simply dummy text of the printing and typesetting industry. Lorem ipsum has been the industry's standard dummy text of the printing industry.</p><span class="btn">MORE INFO</span></div>
  <div class="photo warm" style="left:104px;top:32px;width:76px;height:86px" role="img" aria-label="Presenter speaking to a team at a meeting table"></div>
  <div class="foot"><span>Human Resources services &amp; business coaching.</span><span>BrightPath | 3</span></div>
</section>

<!-- 4 -->
<section class="slide">
  <div class="panel" style="left:0;top:0;width:210px;height:97px"></div>
  <div class="brand left">BrightPath</div>
  <div class="photo desk" style="left:18px;top:34px;width:92px;height:84px" role="img" aria-label="Two colleagues reviewing documents at a white desk"></div>
  <div style="left:119px;top:34px;width:75px"><p class="kicker">Human Resources services</p><h2>YOUR SLIDE<br><b>TITLE GOES HERE</b></h2><p class="sub">Description Here</p><p class="copy">Lorem ipsum is simply dummy text of the printing and typesetting industry. Lorem ipsum has been the industry's standard dummy text of the printing industry.</p></div>
  <div class="foot"><span></span><span>BrightPath | 10</span></div>
</section>

<!-- 5 -->
<section class="slide">
  <div class="brand left">BrightPath</div>
  <div class="panel" style="left:92px;top:73px;width:40px;height:45px"></div>
  <div style="left:16px;top:22px;width:100px"><p class="kicker">Human Resources services</p><h2>YOUR SLIDE<br><b>TITLE GOES HERE</b></h2><p class="copy">Lorem ipsum is simply dummy text of the printing and typesetting industry. Lorem ipsum has been the industry's standard dummy text of the printing and typesetting industry. Lorem ipsum has been the industry's standard dummy text of the printing industry. Lorem ipsum is simply dummy text of the printing and typesetting industry.</p><span class="btn">MORE INFO</span></div>
  <div class="photo desk" style="left:131px;top:0;width:79px;height:92px" role="img" aria-label="Hands typing on a laptop beside a coffee cup"></div>
  <div class="foot"><span>Human Resources services &amp; business coaching.</span><span>BrightPath | 5</span></div>
</section>

<!-- 6 -->
<section class="slide">
  <div class="panel" style="left:0;top:0;width:210px;height:93px"></div>
  <div class="brand">BrightPath</div>
  <div class="photo crowd" style="left:23px;top:0;width:77px;height:118px" role="img" aria-label="Busy crowd of commuters seen from above"></div>
  <div style="left:118px;top:34px;width:75px"><p class="kicker">Human Resources services</p><h2>YOUR SLIDE<br><b>TITLE GOES HERE</b></h2><p class="sub">Description Here</p><p class="copy">Lorem ipsum is simply dummy text of the printing and typesetting industry. Lorem ipsum has been the industry's standard dummy text.</p></div>
  <div class="foot"><span></span><span>BrightPath | 6</span></div>
</section>

<!-- 7 -->
<section class="slide light" style="background:var(--purple)">
  <div class="brand light">BrightPath</div>
  <div style="left:16px;top:29px;width:68px"><p class="kicker">Human Resources services</p><h2>ABOUT BRIGHTPATH VISION<br><span style="font-weight:600">IN STATEMENT.</span></h2><p class="copy">Lorem ipsum is simply dummy text of the printing and typesetting industry. Lorem ipsum has been the industry's standard dummy text of the printing industry.</p><p class="copy">Lorem ipsum is simply dummy text of the printing and typesetting industry. Lorem ipsum has been the industry's standard dummy text.</p></div>
  <div class="photo desk" style="left:104px;top:28px;width:88px;height:75px" role="img" aria-label="Businessman signing papers at a desk"></div>
  <div class="foot" style="color:#d8cde8"><span>Human Resources services &amp; business coaching.</span><span>BrightPath | 7</span></div>
</section>

<!-- 8 -->
<section class="slide">
  <div class="panel" style="left:0;top:0;width:210px;height:97px"></div>
  <div class="brand left">BrightPath</div>
  <div class="photo warm" style="left:0;top:25px;width:55px;height:93px" role="img" aria-label="Man writing beside an hourglass"></div>
  <div style="left:64px;top:34px;width:62px"><p class="kicker">Human Resources services</p><h2>YOUR SLIDE<br><b>TITLE GOES HERE</b></h2><p class="sub">Description Here</p><p class="copy">Lorem ipsum is simply dummy text of the printing and typesetting industry. Lorem ipsum has been the industry's standard dummy text of the printing industry.</p></div>
  <div style="left:190px;top:75px;width:20px;height:35px;background:var(--orange)"></div>
  <div class="photo desk" style="left:133px;top:0;width:72px;height:100px" role="img" aria-label="Laptop and coffee cup on a desk from above"></div>
  <div class="foot"><span></span><span>BrightPath | 8</span></div>
</section>

<!-- 9 -->
<section class="slide">
  <div class="panel" style="left:0;top:0;width:110px;height:118px"></div>
  <div style="left:17px;top:19px"><p class="kicker">About Our CEO</p><h2>MEET OUR<br><b>TEAM LEADER</b></h2></div>
  <div class="photo desk" style="left:105px;top:0;width:105px;height:118px" role="img" aria-label="Hands typing on a laptop with coffee on a white desk"></div>
  <div style="left:17px;top:63px;width:120px;height:34px;background:var(--purple)"></div>
  <div class="photo warm" style="left:27px;top:55px;width:38px;height:34px" role="img" aria-label="Portrait of the team leader presenting"></div>
  <div class="light" style="left:78px;top:68px;width:55px"><p class="kicker" style="font-weight:700">MARTIN HALE</p><p class="copy">Lorem ipsum is simply dummy text of the printing and typesetting industry. Lorem ipsum has been the industry.</p></div>
  <div class="foot"><span>Human Resources services &amp; business coaching.</span><span>BrightPath | 9</span></div>
</section>

<!-- 10 -->
<section class="slide">
  <div class="panel" style="left:0;top:0;width:210px;height:118px"></div>
  <div class="brand">BrightPath</div>
  <div class="photo warm" style="left:17px;top:22px;width:75px;height:96px" role="img" aria-label="Man writing at a laptop with an hourglass"></div>
  <div style="left:118px;top:22px;width:75px"><p class="kicker">Human Resources services</p><h2>YOUR SLIDE<br><b>TITLE GOES HERE</b></h2><p class="copy">Lorem ipsum is simply dummy text of the printing and typesetting industry. Lorem ipsum has been the industry's standard dummy text of the printing and typesetting industry. Lorem ipsum has been the industry's standard dummy text.</p><p class="copy">Lorem ipsum is simply dummy text of the printing and typesetting industry. Lorem ipsum has been the industry's standard dummy text.</p></div>
  <div class="foot"><span>Human Resources services &amp; business coaching.</span><span>BrightPath | 4</span></div>
</section>

<!-- 11 -->
<section class="slide">
  <div style="left:0;top:0;width:210px;height:60px;background:var(--purple)"></div>
  <div class="photo crowd" style="left:0;top:60px;width:210px;height:58px" role="img" aria-label="Crowd walking through a modern lobby"></div>
  <div class="brand light">BrightPath</div>
  <div class="light" style="left:110px;top:27px;width:80px"><p class="kicker">Human Resources services</p><h2>WHAT WE DO</h2><p class="copy">Lorem ipsum is simply dummy text of the printing and typesetting industry. Lorem ipsum has been the industry.</p></div>
  <div class="card" style="left:17px;top:26px;width:64px;height:19px"><strong>Description Here</strong>Lorem ipsum is simply dummy text simply dummy text.</div>
  <div class="card" style="left:17px;top:53px;width:64px;height:19px"><strong>Description Here</strong>Lorem ipsum is simply dummy text simply dummy text.</div>
  <div class="card" style="left:17px;top:80px;width:64px;height:19px"><strong>Description Here</strong>Lorem ipsum is simply dummy text simply dummy text.</div>
  <svg style="left:70px;top:30px" width="8" height="70" viewBox="0 0 8 70" fill="none" stroke="#f5a623" stroke-width=".6"><path d="M1 5 7 1 5 7 4 4Z"/><rect x="1" y="28" width="6" height="5"/><circle cx="4" cy="58" r="3"/></svg>
  <div class="foot" style="color:#ddd"><span></span><span>BrightPath | 11</span></div>
</section>

<!-- 12 -->
<section class="slide">
  <div class="brand">BrightPath</div>
  <div class="photo crowd" style="left:26px;top:0;width:38px;height:116px" role="img" aria-label="Crowd seen from above"></div>
  <div class="photo desk" style="left:66px;top:22px;width:40px;height:42px" role="img" aria-label="Colleagues reviewing notes"></div>
  <div class="photo desk" style="left:66px;top:66px;width:40px;height:45px" role="img" aria-label="Hands typing on a laptop"></div>
  <div style="left:133px;top:29px;width:60px"><h2>WHAT <b>WE DO</b></h2>
    <p class="sub">Description Here</p><p class="copy">Lorem ipsum is simply dummy text simply dummy text.</p>
    <p class="sub">Description Here</p><p class="copy">Lorem ipsum is simply dummy text simply dummy text.</p>
    <p class="sub">Description Here</p><p class="copy">Lorem ipsum is simply dummy text simply dummy text.</p></div>
  <div class="foot"><span>Human Resources services &amp; business coaching.</span><span>BrightPath | 12</span></div>
</section>

<!-- 13 break -->
<section class="slide">
  <div class="brand">BrightPath</div>
  <div class="photo violet" style="left:0;top:22px;width:210px;height:96px" role="img" aria-label="Team meeting around laptops in a purple tint"></div>
  <h2 style="left:18px;top:57px;font-size:13px;color:#fff;font-weight:400">BREAK <span style="color:var(--orange)">SLIDE</span></h2>
  <span class="btn orange" style="left:20px;top:89px;margin:0">MORE INFO</span>
</section>

<!-- 14 -->
<section class="slide">
  <div class="brand">BrightPath</div>
  <div style="left:16px;top:25px"><p class="kicker">Human Resources services</p><h2>YOUR SLIDE<br><b>TITLE GOES HERE</b></h2></div>
  <p class="copy" style="left:88px;top:24px;width:105px">Lorem ipsum is simply dummy text of the printing and typesetting industry. Lorem ipsum has been the industry's standard dummy text of the printing and typesetting industry. Lorem ipsum has been the industry's standard dummy text of the printing industry.</p>
  <div class="photo desk" style="left:18px;top:59px;width:118px;height:59px" role="img" aria-label="Colleagues reviewing documents at a desk"></div>
  <div class="photo desk" style="left:140px;top:59px;width:52px;height:50px" role="img" aria-label="Laptop and coffee on a desk"></div>
  <div class="foot"><span></span><span>BrightPath | 14</span></div>
</section>

<!-- 15 -->
<section class="slide">
  <div class="brand">BrightPath</div>
  <h2 class="hd" style="left:19px;top:16px">YOUR SLIDE <b>TITLE GOES HERE</b></h2>
  <div class="photo warm" style="left:17px;top:32px;width:63px;height:53px" role="img" aria-label="Team working together at a meeting table"></div>
  <div class="photo warm" style="left:84px;top:32px;width:63px;height:53px" role="img" aria-label="Woman working on a laptop"></div>
  <div class="photo desk" style="left:151px;top:32px;width:59px;height:53px" role="img" aria-label="Hands on a laptop keyboard"></div>
  <p class="cap" style="left:19px;top:89px;width:58px"><strong>Lorem ipsum</strong> is simply dummy text of the printing industry.</p>
  <p class="cap" style="left:86px;top:89px;width:58px"><strong>Lorem ipsum</strong> is simply dummy text of the printing industry.</p>
  <p class="cap" style="left:153px;top:89px;width:55px"><strong>Lorem ipsum</strong> is simply dummy text of the printing industry.</p>
  <div class="foot"><span>Human Resources services &amp; business coaching.</span><span>BrightPath | 15</span></div>
</section>

<!-- 16 -->
<section class="slide">
  <div class="brand">BrightPath</div>
  <div style="left:16px;top:25px"><p class="kicker">Human Resources services</p><h2>YOUR SLIDE<br><b>TITLE GOES HERE</b></h2></div>
  <p class="copy" style="left:86px;top:24px;width:108px">Lorem ipsum is simply dummy text of the printing and typesetting industry. Lorem ipsum has been the industry's standard dummy text of the printing and typesetting industry. Lorem ipsum has been the industry's standard dummy text.</p>
  <div class="photo warm" style="left:0;top:59px;width:130px;height:59px" role="img" aria-label="Team meeting around laptops"></div>
  <ul class="copy" style="left:142px;top:60px;width:52px;padding-left:3px">
    <li>Lorem ipsum is simply dummy text of the printing industry.</li>
    <li>Lorem ipsum has been the industry's standard dummy text of the printing.</li>
    <li>Industry lorem ipsum has been the typesetting industry.</li>
  </ul>
  <div class="foot"><span></span><span>BrightPath | 16</span></div>
</section>

<!-- 17 -->
<section class="slide">
  <div class="brand">BrightPath</div>
  <div class="photo warm" style="left:0;top:21px;width:95px;height:76px" role="img" aria-label="Woman working at a laptop in a bright office"></div>
  <div style="left:108px;top:25px"><p class="kicker">Human Resources services</p><h2>YOUR SLIDE<br><b>TITLE GOES HERE</b></h2></div>
  <div class="panel" style="left:98px;top:52px;width:112px;height:58px"></div>
  <ul class="copy" style="left:106px;top:54px;width:92px;padding-left:3px">
    <li>Lorem ipsum is simply dummy text of the printing and typesetting industry. Lorem ipsum has been the industry's standard dummy text.</li>
    <li>Lorem ipsum has been the industry's standard dummy text of the printing and typesetting industry.</li>
    <li>Lorem ipsum has been the industry's standard dummy text of simply dummy text.</li>
  </ul>
  <div class="foot"><span>Human Resources services &amp; business coaching.</span><span>BrightPath | 17</span></div>
</section>

<!-- 18 -->
<section class="slide">
  <div class="brand">BrightPath</div>
  <h2 class="hd" style="top:8px;left:15px">YOUR SLIDE <b>TITLE GOES HERE</b></h2>
  <div class="photo desk" style="left:0;top:21px;width:69px;height:86px" role="img" aria-label="Colleagues reviewing documents"></div>
  <div class="photo warm" style="left:71px;top:21px;width:69px;height:86px" role="img" aria-label="Presenter addressing a team"></div>
  <div class="photo warm" style="left:142px;top:21px;width:68px;height:86px" role="img" aria-label="Team working on laptops"></div>
  <div class="foot"><span>Human Resources services &amp; business coaching.</span><span>BrightPath | 18</span></div>
</section>

<!-- 19 -->
<section class="slide">
  <div class="brand">BrightPath</div>
  <div class="panel" style="left:0;top:0;width:91px;height:118px"></div>
  <div style="left:16px;top:24px;width:68px"><p class="kicker">Human Resources services</p><h2>YOUR SLIDE<br><b>TITLE GOES HERE</b></h2><p class="sub">Description Here</p><p class="copy">Lorem ipsum is simply dummy text of the printing and typesetting industry. Lorem ipsum has been the industry's standard dummy text of the printing industry.</p><p class="copy">Lorem ipsum is simply dummy text of the printing and typesetting industry. Lorem ipsum has been the industry's standard dummy text.</p></div>
  <div class="photo warm" style="left:92px;top:24px;width:72px;height:94px" role="img" aria-label="Businessman writing beside an hourglass"></div>
  <div class="card" style="left:122px;top:73px;width:66px;height:20px"><strong>Description Here</strong>Lorem ipsum is simply dummy text simply dummy text.</div>
  <svg style="left:180px;top:80px" width="6" height="6" viewBox="0 0 8 8" fill="none" stroke="#f5a623" stroke-width=".8"><path d="M1 5 7 1 5 7 4 4Z"/></svg>
  <div class="foot"><span></span><span>BrightPath | 13</span></div>
</section>

<!-- 20 six options -->
<section class="slide">
  <div class="brand">BrightPath</div>
  <h2 class="hd" style="top:8px;left:17px">YOUR SLIDE <b>TITLE GOES HERE</b></h2>
  <svg style="left:0;top:0" width="210" height="118" viewBox="0 0 210 118">
    <g fill="none" stroke="#e3e0ea" stroke-width="2.4">
      <circle cx="42" cy="62" r="12"/><circle cx="68" cy="62" r="12"/><circle cx="94" cy="62" r="12"/><circle cx="120" cy="62" r="12"/><circle cx="146" cy="62" r="12"/><circle cx="172" cy="62" r="12"/>
    </g>
    <g fill="#fff" stroke-width="1.2">
      <circle cx="42" cy="62" r="9" stroke="#66379b"/><circle cx="68" cy="62" r="9" stroke="#f5a623"/><circle cx="94" cy="62" r="9" stroke="#3a5cc4"/><circle cx="120" cy="62" r="9" stroke="#ef5a7a"/><circle cx="146" cy="62" r="9" stroke="#17a196"/><circle cx="172" cy="62" r="9" stroke="#f5a623"/>
    </g>
    <g font-size="3" text-anchor="middle" fill="#2b2b33">
      <text x="42" y="60">Option</text><text x="68" y="60">Option</text><text x="94" y="60">Option</text><text x="120" y="60">Option</text><text x="146" y="60">Option</text><text x="172" y="60">Option</text>
      <text x="42" y="65" font-weight="700" fill="#66379b">A</text><text x="68" y="65" font-weight="700" fill="#66379b">B</text><text x="94" y="65" font-weight="700" fill="#66379b">C</text><text x="120" y="65" font-weight="700" fill="#66379b">D</text><text x="146" y="65" font-weight="700" fill="#66379b">E</text><text x="172" y="65" font-weight="700" fill="#66379b">F</text>
    </g>
    <g stroke="#c7bedb" stroke-width=".4" stroke-dasharray="1 1"><path d="M42 49V36M94 49V36M146 49V36M68 75V88M120 75V88M172 75V88"/></g>
  </svg>
  <p class="lbl" style="left:28px;top:24px;width:28px"><strong>Option One</strong>A peep at some distant orb has power to raise and purify.</p>
  <p class="lbl" style="left:80px;top:24px;width:28px"><strong>Option Three</strong>Distant orb has power to raise and purify our thoughts.</p>
  <p class="lbl" style="left:132px;top:24px;width:28px"><strong>Option Five</strong>Power to raise and purify our thoughts like a strain.</p>
  <p class="lbl" style="left:54px;top:90px;width:28px"><strong>Option Two</strong>A peep at some distant orb has power to raise.</p>
  <p class="lbl" style="left:106px;top:90px;width:28px"><strong>Option Four</strong>Power to raise and purify our thoughts.</p>
  <p class="lbl" style="left:158px;top:90px;width:28px"><strong>Option Six</strong>Distant orb has power to raise and purify.</p>
  <div class="foot"><span>Human Resources services &amp; business coaching.</span><span>BrightPath | 22</span></div>
</section>

<!-- 21 timeline -->
<section class="slide">
  <div class="brand">BrightPath</div>
  <h2 class="hd" style="top:8px">THE <b>TIMELINE</b></h2>
  <div style="left:17px;top:49px;width:193px;height:7px;background:var(--panel)"></div>
  <div style="left:88px;top:49px;width:51px;height:7px;background:var(--purple)"></div>
  <p class="sub" style="left:37px;top:48.5px;font-size:2.6px;margin:0">2010</p>
  <p class="sub" style="left:90px;top:48.5px;font-size:2.6px;margin:0;color:#fff">2011</p>
  <p class="sub" style="left:142px;top:48.5px;font-size:2.6px;margin:0">2013</p>
  <div style="left:37px;top:63px;width:46px"><p class="sub" style="margin:0">History title</p><p class="copy" style="color:var(--ink)">A peep at some distant orb has power to raise and purify our thoughts like a strain of sacred music, or a noble picture. It always does one good.</p></div>
  <div style="left:90px;top:63px;width:46px"><p class="sub" style="margin:0">History title</p><p class="copy">Like a strain of sacred music, or a noble picture, or a passage from the grander poets. It always does one good.</p></div>
  <div style="left:142px;top:63px;width:46px"><p class="sub" style="margin:0">History title</p><p class="copy">A peep at some distant orb has power to raise and purify our thoughts like a strain of sacred music. It always does one good.</p></div>
  <div class="foot"><span>Human Resources services &amp; business coaching.</span><span>BrightPath | 20</span></div>
</section>

<section class="slide">
  <div class="brand">BrightPath</div>
  <h2 class="hd" style="top:8px">THE <b>TIMELINE</b></h2>
  <div style="left:0;top:49px;width:193px;height:7px;background:var(--panel)"></div>
  <div style="left:70px;top:49px;width:52px;height:7px;background:var(--purple)"></div>
  <p class="sub" style="left:20px;top:48.5px;font-size:2.6px;margin:0">2014</p>
  <p class="sub" style="left:72px;top:48.5px;font-size:2.6px;margin:0;color:#fff">2018</p>
  <p class="sub" style="left:124px;top:48.5px;font-size:2.6px;margin:0">2023</p>
  <div style="left:20px;top:63px;width:46px"><p class="sub" style="margin:0">History title</p><p class="copy" style="color:var(--ink)">A peep at some distant orb has power to raise and purify our thoughts like a strain of sacred music, or a noble picture. It always does one good.</p></div>
  <div style="left:72px;top:63px;width:46px"><p class="sub" style="margin:0">History title</p><p class="copy">Like a strain of sacred music, or a noble picture, or a passage from the grander poets. It always does one good.</p></div>
  <div style="left:124px;top:63px;width:46px"><p class="sub" style="margin:0">History title</p><p class="copy">A peep at some distant orb has power to raise and purify our thoughts like a strain of sacred music. It always does one good.</p></div>
  <div class="foot"><span>Human Resources services &amp; business coaching.</span><span>BrightPath | 21</span></div>
</section>

<!-- 23 five options -->
<section class="slide">
  <div class="brand">BrightPath</div>
  <h2 class="hd" style="top:8px;left:17px">YOUR SLIDE <b>TITLE GOES HERE</b></h2>
  <svg style="left:0;top:0" width="210" height="118" viewBox="0 0 210 118">
    <rect x="34" y="54" width="144" height="27" rx="13.5" fill="none" stroke="#e6e4ea" stroke-width="1.4"/>
    <circle cx="51" cy="67.5" r="10" fill="#66379b"/><circle cx="78" cy="67.5" r="10" fill="#f5a623"/><circle cx="105" cy="67.5" r="10" fill="#ef5a7a"/><circle cx="132" cy="67.5" r="10" fill="#17a196"/><circle cx="159" cy="67.5" r="10" fill="#f1e6b8"/>
    <g font-size="3" text-anchor="middle" fill="#fff">
      <text x="51" y="66">Option</text><text x="78" y="66">Option</text><text x="105" y="66">Option</text><text x="132" y="66">Option</text><text x="159" y="66">Option</text>
      <text x="51" y="71" font-weight="700">A</text><text x="78" y="71" font-weight="700">B</text><text x="105" y="71" font-weight="700">C</text><text x="132" y="71" font-weight="700">D</text><text x="159" y="71" font-weight="700">E</text>
    </g>
  </svg>
  <p class="lbl" style="left:37px;top:24px;width:28px"><strong>Option One</strong>A peep at some distant orb has power to raise and purify.</p>
  <p class="lbl" style="left:91px;top:24px;width:28px"><strong>Option Three</strong>Distant orb has power to raise and purify our thoughts.</p>
  <p class="lbl" style="left:145px;top:24px;width:28px"><strong>Option Five</strong>Power to raise and purify our thoughts like a strain.</p>
  <p class="lbl" style="left:64px;top:93px;width:28px"><strong>Option Two</strong>A peep at some distant orb has power to raise.</p>
  <p class="lbl" style="left:118px;top:93px;width:28px"><strong>Option Four</strong>Power to raise and purify our thoughts.</p>
  <div class="foot"><span>Human Resources services &amp; business coaching.</span><span>BrightPath | 23</span></div>
</section>

<!-- 24 six ring -->
<section class="slide">
  <div class="brand">BrightPath</div>
  <h2 class="hd" style="top:8px;left:17px">YOUR SLIDE <b>TITLE GOES HERE</b></h2>
  <svg style="left:0;top:0" width="210" height="118" viewBox="0 0 210 118">
    <g transform="rotate(-90 105 68)" fill="none" stroke-width="12">
      <circle cx="105" cy="68" r="17" pathLength="100" stroke="#f5a623" stroke-dasharray="16 84" stroke-dashoffset="0"/>
      <circle cx="105" cy="68" r="17" pathLength="100" stroke="#17a196" stroke-dasharray="16 84" stroke-dashoffset="-16.67"/>
      <circle cx="105" cy="68" r="17" pathLength="100" stroke="#127a72" stroke-dasharray="16 84" stroke-dashoffset="-33.33"/>
      <circle cx="105" cy="68" r="17" pathLength="100" stroke="#66379b" stroke-dasharray="16 84" stroke-dashoffset="-50"/>
      <circle cx="105" cy="68" r="17" pathLength="100" stroke="#7d52b2" stroke-dasharray="16 84" stroke-dashoffset="-66.67"/>
      <circle cx="105" cy="68" r="17" pathLength="100" stroke="#ef5a7a" stroke-dasharray="16 84" stroke-dashoffset="-83.33"/>
    </g>
    <circle cx="105" cy="68" r="8" fill="#fff"/><circle cx="105" cy="68" r="4" fill="#66379b"/>
    <g font-size="2.6" text-anchor="middle" fill="#fff">
      <text x="113" y="52">Option</text><text x="113" y="55.5" font-weight="700">01</text>
      <text x="122" y="66">Option</text><text x="122" y="69.5" font-weight="700">02</text>
      <text x="113" y="81">Option</text><text x="113" y="84.5" font-weight="700">03</text>
      <text x="97" y="81">Option</text><text x="97" y="84.5" font-weight="700">04</text>
      <text x="88" y="66">Option</text><text x="88" y="69.5" font-weight="700">05</text>
      <text x="97" y="52">Option</text><text x="97" y="55.5" font-weight="700">06</text>
    </g>
  </svg>
  <p class="lbl" style="left:50px;top:24px;width:30px"><strong>Strategy</strong>Raise and purify our thoughts like a strain.</p>
  <p class="lbl" style="left:35px;top:53px;width:30px"><strong>Start Up</strong>A peep at some distant orb has power.</p>
  <p class="lbl" style="left:45px;top:88px;width:30px"><strong>Overview</strong>Power to raise and purify our thoughts.</p>
  <p class="lbl" style="left:140px;top:24px;width:30px;text-align:left"><strong>Overview</strong>Power to raise and purify our thoughts.</p>
  <p class="lbl" style="left:148px;top:55px;width:30px;text-align:left"><strong>Business model</strong>A peep at some distant orb has power.</p>
  <p class="lbl" style="left:140px;top:88px;width:30px;text-align:left"><strong>Controller</strong>Purify our thoughts like a strain.</p>
  <div class="foot"><span>Human Resources services &amp; business coaching.</span><span>BrightPath | 24</span></div>
</section>

<!-- 25 four ring -->
<section class="slide">
  <div class="brand">BrightPath</div>
  <h2 class="hd" style="top:8px;left:17px">YOUR SLIDE <b>TITLE GOES HERE</b></h2>
  <svg style="left:0;top:0" width="210" height="118" viewBox="0 0 210 118">
    <g transform="rotate(-90 97 67)" fill="none" stroke-width="17">
      <circle cx="97" cy="67" r="19" pathLength="100" stroke="#66379b" stroke-dasharray="24 76" stroke-dashoffset="-.5"/>
      <circle cx="97" cy="67" r="19" pathLength="100" stroke="#f5a623" stroke-dasharray="24 76" stroke-dashoffset="-25.5"/>
      <circle cx="97" cy="67" r="19" pathLength="100" stroke="#ef5a7a" stroke-dasharray="24 76" stroke-dashoffset="-50.5"/>
      <circle cx="97" cy="67" r="19" pathLength="100" stroke="#17a196" stroke-dasharray="24 76" stroke-dashoffset="-75.5"/>
    </g>
    <circle cx="97" cy="67" r="9" fill="#fff"/><circle cx="97" cy="67" r="4.5" fill="#66379b"/>
    <g font-size="3" text-anchor="middle" fill="#fff">
      <text x="84" y="56">Option</text><text x="84" y="60" font-weight="700">04</text>
      <text x="110" y="56">Option</text><text x="110" y="60" font-weight="700">01</text>
      <text x="84" y="78">Option</text><text x="84" y="82" font-weight="700">03</text>
      <text x="110" y="78">Option</text><text x="110" y="82" font-weight="700">02</text>
    </g>
  </svg>
  <p class="lbl" style="left:35px;top:27px;width:30px;text-align:right"><strong>Start Up</strong>A peep at some distant orb has power.</p>
  <p class="lbl" style="left:32px;top:86px;width:30px;text-align:right"><strong>Overview</strong>Power to raise and purify our thoughts.</p>
  <p class="lbl" style="left:140px;top:27px;width:30px;text-align:left"><strong>Overview</strong>Power to raise and purify our thoughts.</p>
  <p class="lbl" style="left:140px;top:86px;width:30px;text-align:left"><strong>Business model</strong>A peep at some distant orb has power.</p>
  <div class="foot"><span>Human Resources services &amp; business coaching.</span><span>BrightPath | 25</span></div>
</section>

<!-- 26 core values -->
<section class="slide">
  <div class="brand">BrightPath</div>
  <h2 class="hd" style="top:8px;left:17px">YOUR SLIDE <b>TITLE GOES HERE</b></h2>
  <svg style="left:0;top:0" width="210" height="118" viewBox="0 0 210 118">
    <circle cx="106" cy="68" r="22" fill="none" stroke="#ddd" stroke-width=".5"/>
    <circle cx="106" cy="44" r="7" fill="#66379b"/><circle cx="128" cy="61" r="7" fill="#f5a623"/><circle cx="120" cy="88" r="7" fill="#ef5a7a"/><circle cx="92" cy="88" r="7" fill="#17a196"/><circle cx="84" cy="61" r="7" fill="#f1e6b8"/>
    <g font-size="2.2" text-anchor="middle" fill="#fff">
      <text x="106" y="43.5">Core</text><text x="106" y="46.5">value</text>
      <text x="128" y="60.5">Core</text><text x="128" y="63.5">value</text>
      <text x="120" y="87.5">Core</text><text x="120" y="90.5">value</text>
      <text x="92" y="87.5">Core</text><text x="92" y="90.5">value</text>
      <text x="84" y="60.5">Core</text><text x="84" y="63.5">value</text>
    </g>
    <text x="106" y="70" font-size="3.6" text-anchor="middle" fill="#2b2b33">Core Values</text>
  </svg>
  <p class="lbl" style="left:122px;top:28px;width:40px;text-align:left"><strong>Overview</strong>A peep at some distant orb has power to raise.</p>
  <p class="lbl" style="left:148px;top:57px;width:40px;text-align:left"><strong>Devices</strong>A peep at some distant orb has power to raise.</p>
  <p class="lbl" style="left:136px;top:84px;width:40px;text-align:left"><strong>Infographics</strong>A peep at some distant orb has power.</p>
  <p class="lbl" style="left:35px;top:57px;width:40px;text-align:right"><strong>Solutions</strong>Distant orb has power to raise and purify.</p>
  <p class="lbl" style="left:38px;top:84px;width:45px;text-align:right"><strong>Web design</strong>A peep at some distant orb has power to raise.</p>
  <div class="foot"><span>Human Resources services &amp; business coaching.</span><span>BrightPath | 26</span></div>
</section>

<!-- 27 process -->
<section class="slide">
  <div class="brand">BrightPath</div>
  <h2 class="hd" style="top:8px;left:17px">PROCESS STEP <b>INFOGRAPHIC</b></h2>
  <svg style="left:0;top:0" width="210" height="118" viewBox="0 0 210 118">
    <rect x="30" y="34" width="160" height="48" rx="24" fill="none" stroke="#e4e2e8" stroke-width="2.4"/>
    <polygon points="42,44 70,44 74,49 70,54 42,54" fill="#66379b"/>
    <polygon points="70,44 97,44 101,49 97,54 70,54 74,49" fill="#f5a623"/>
    <polygon points="97,44 124,44 128,49 124,54 97,54 101,49" fill="#ef5a7a"/>
    <polygon points="124,44 151,44 155,49 151,54 124,54 128,49" fill="#17a196"/>
    <polygon points="151,44 176,44 180,49 176,54 151,54 155,49" fill="#f1e6b8"/>
    <g font-size="2.6" fill="#fff" text-anchor="middle"><text x="57" y="50">Option 01</text><text x="86" y="50">Option 02</text><text x="113" y="50">Option 03</text><text x="140" y="50">Option 04</text><text x="166" y="50">Option 05</text></g>
  </svg>
  <p class="lbl" style="left:42px;top:57px;width:26px;text-align:left"><strong>Write title here</strong>A peep at some distant orb has power.</p>
  <p class="lbl" style="left:70px;top:57px;width:26px;text-align:left"><strong>Write title here</strong>Some distant orb has power to raise.</p>
  <p class="lbl" style="left:97px;top:57px;width:26px;text-align:left"><strong>Write title here</strong>At some distant orb has power to raise.</p>
  <p class="lbl" style="left:124px;top:57px;width:26px;text-align:left"><strong>Write title here</strong>Distant orb has power to raise.</p>
  <p class="lbl" style="left:151px;top:57px;width:26px;text-align:left"><strong>Write title here</strong>Distant orb has power to raise.</p>
  <div class="foot"><span>Human Resources services &amp; business coaching.</span><span>BrightPath | 27</span></div>
</section>

<!-- 28 clustered chart -->
<section class="slide">
  <div class="brand">BrightPath</div>
  <h2 class="hd" style="top:8px;left:17px">CLUSTERED <b>CHART STYLE</b></h2>
  <div style="left:17px;top:31px;width:55px"><p class="sub" style="margin:0">Subtitle</p><p class="copy" style="color:var(--ink)">Lorem ipsum is simply dummy text of the printing and typesetting industry. Lorem ipsum has been the industry's standard dummy text of simply dummy text.</p><p class="copy" style="color:var(--ink)">Lorem ipsum has been the industry's standard dummy text of the printing and typesetting industry.</p><p class="copy" style="color:var(--ink)">Lorem ipsum has been the industry's standard dummy text of simply dummy text.</p></div>
  <svg style="left:0;top:0" width="210" height="118" viewBox="0 0 210 118">
    <g font-size="1.8" fill="#888"><rect x="138" y="23" width="2" height="2" fill="#66379b"/><text x="141" y="25">Series 1</text><rect x="150" y="23" width="2" height="2" fill="#f5a623"/><text x="153" y="25">Series 2</text><rect x="162" y="23" width="2" height="2" fill="#ef5a7a"/><text x="165" y="25">Series 3</text></g>
    <g stroke="#eee" stroke-width=".3"><path d="M128 36H200M128 50H200M128 64H200M128 78H200M128 92H200"/></g>
    <path d="M128 106H200" stroke="#ccc" stroke-width=".4"/>
    <g font-size="1.8" fill="#888" text-anchor="end"><text x="125" y="107">0</text><text x="125" y="93">1</text><text x="125" y="79">2</text><text x="125" y="65">3</text><text x="125" y="51">4</text><text x="125" y="37">5</text></g>
    <g fill="#66379b"><rect x="132" y="45.8" width="3" height="60.2"/><rect x="150" y="71" width="3" height="35"/><rect x="168" y="57" width="3" height="49"/><rect x="186" y="43" width="3" height="63"/></g>
    <g fill="#f5a623"><rect x="135" y="72.4" width="3" height="33.6"/><rect x="153" y="44.4" width="3" height="61.6"/><rect x="171" y="80.8" width="3" height="25.2"/><rect x="189" y="66.8" width="3" height="39.2"/></g>
    <g fill="#ef5a7a"><rect x="138" y="78" width="3" height="28"/><rect x="156" y="78" width="3" height="28"/><rect x="174" y="64" width="3" height="42"/><rect x="192" y="36" width="3" height="70"/></g>
    <g font-size="1.8" fill="#888" text-anchor="middle"><text x="137" y="110">Category 1</text><text x="155" y="110">Category 2</text><text x="173" y="110">Category 3</text><text x="191" y="110">Category 4</text></g>
  </svg>
  <div class="foot"><span>Human Resources services &amp; business coaching.</span><span>BrightPath | 28</span></div>
</section>

<!-- 29 pie -->
<section class="slide">
  <div class="brand">BrightPath</div>
  <h2 class="hd" style="top:8px;left:17px">PIE <b>CHART STYLE</b></h2>
  <div style="left:17px;top:31px;width:55px"><p class="sub" style="margin:0">Subtitle</p><p class="copy" style="color:var(--ink)">Lorem ipsum is simply dummy text of the printing and typesetting industry. Lorem ipsum has been the industry's standard dummy text of simply dummy text.</p><p class="copy" style="color:var(--ink)">Lorem ipsum has been the industry's standard dummy text of the printing and typesetting industry.</p><p class="copy" style="color:var(--ink)">Lorem ipsum has been the industry's standard dummy text of simply dummy text.</p></div>
  <svg style="left:0;top:0" width="210" height="118" viewBox="0 0 210 118">
    <text x="136" y="19" font-size="2.4" text-anchor="middle" fill="#444">Series 1</text>
    <g transform="translate(137 67) scale(1.15)">
      <path d="M0 0 0 -20A20 20 0 0 1 19.37 4.97Z" fill="#17a196"/>
      <path d="M0 0 19.37 4.97A20 20 0 0 1 4.97 19.37Z" fill="#ef5a7a"/>
      <path d="M0 0 4.97 19.37A20 20 0 0 1 -19.02 6.18Z" fill="#f5a623"/>
      <path d="M0 0 -19.02 6.18A20 20 0 0 1 0 -20Z" fill="#66379b"/>
    </g>
    <g font-size="2" fill="#fff" text-anchor="middle"><text x="148" y="56">Category 1</text><text x="148" y="59">29%</text><text x="148" y="77">Category 2</text><text x="148" y="80">17%</text><text x="128" y="84">Category 3</text><text x="128" y="87">24%</text><text x="124" y="60">Category 4</text><text x="124" y="63">30%</text></g>
  </svg>
  <div class="foot"><span>Human Resources services &amp; business coaching.</span><span>BrightPath | 29</span></div>
</section>

<!-- 30 area -->
<section class="slide">
  <div class="brand">BrightPath</div>
  <h2 class="hd" style="top:8px;left:17px">AREA <b>CHART STYLE</b></h2>
  <div style="left:17px;top:31px;width:55px"><p class="sub" style="margin:0">Subtitle</p><p class="copy" style="color:var(--ink)">Lorem ipsum is simply dummy text of the printing and typesetting industry. Lorem ipsum has been the industry's standard dummy text of simply dummy text.</p><p class="copy" style="color:var(--ink)">Lorem ipsum has been the industry's standard dummy text of the printing and typesetting industry.</p><p class="copy" style="color:var(--ink)">Lorem ipsum has been the industry's standard dummy text of simply dummy text.</p></div>
  <svg style="left:0;top:0" width="210" height="118" viewBox="0 0 210 118">
    <g font-size="1.8" fill="#888"><path d="M118 23h4" stroke="#17a196" stroke-width=".6"/><text x="123" y="24">Series 1</text><path d="M134 23h4" stroke="#66379b" stroke-width=".6"/><text x="139" y="24">Series 2</text></g>
    <g font-size="1.8" fill="#888" text-anchor="end"><text x="90" y="101">0</text><text x="90" y="88">1</text><text x="90" y="75">2</text><text x="90" y="62">3</text><text x="90" y="49">4</text><text x="90" y="36">5</text><text x="90" y="23">6</text></g>
    <g font-size="1.8" fill="#888" text-anchor="middle"><text x="94" y="105">0</text><text x="113" y="105">1</text><text x="132" y="105">2</text><text x="151" y="105">3</text><text x="170" y="105">4</text><text x="189" y="105">5</text></g>
    <path d="M113 62C122 48 127 70 132 76S142 80 151 70 166 58 170 52" fill="none" stroke="#17a196" stroke-width=".8"/>
    <path d="M113 82C120 74 126 58 132 60S144 78 151 70 164 60 170 56" fill="none" stroke="#66379b" stroke-width=".8"/>
    <path d="M151 72 170 50" fill="none" stroke="#f5a623" stroke-width=".8"/>
  </svg>
  <div class="foot"><span>Human Resources services &amp; business coaching.</span><span>BrightPath | 30</span></div>
</section>

<!-- 31 donut -->
<section class="slide">
  <div class="brand">BrightPath</div>
  <h2 class="hd" style="top:8px;left:17px">DATA <b>OVERVIEW</b></h2>
  <div style="left:17px;top:31px;width:55px"><p class="sub" style="margin:0">Subtitle</p><p class="copy" style="color:var(--ink)">Lorem ipsum is simply dummy text of the printing and typesetting industry. Lorem ipsum has been the industry's standard dummy text of simply dummy text.</p><p class="copy" style="color:var(--ink)">Lorem ipsum has been the industry's standard dummy text of the printing and typesetting industry.</p><p class="copy" style="color:var(--ink)">Lorem ipsum has been the industry's standard dummy text of simply dummy text.</p></div>
  <svg style="left:0;top:0" width="210" height="118" viewBox="0 0 210 118">
    <g transform="rotate(-90 143 67)" fill="none" stroke-width="5">
      <circle cx="143" cy="67" r="17" pathLength="100" stroke="#66379b" stroke-dasharray="55 45"/>
      <circle cx="143" cy="67" r="17" pathLength="100" stroke="#ef5a7a" stroke-dasharray="28 72" stroke-dashoffset="-56"/>
      <circle cx="143" cy="67" r="17" pathLength="100" stroke="#f1e6b8" stroke-dasharray="9 91" stroke-dashoffset="-85"/>
    </g>
    <text x="143" y="68" font-size="3.6" text-anchor="middle" fill="#2b2b33">2019</text>
    <g font-size="1.9" font-weight="700" fill="#2b2b33"><text x="120" y="30">$28.000</text><text x="106" y="45">$32.000</text><text x="168" y="51">$180.000</text><text x="103" y="71">$95.000</text></g>
    <g font-size="1.8" fill="#888"><rect x="117" y="102" width="1.5" height="1.5" fill="#66379b"/><text x="119" y="103.5">May</text><rect x="128" y="102" width="1.5" height="1.5" fill="#ef5a7a"/><text x="130" y="103.5">June</text><rect x="140" y="102" width="1.5" height="1.5" fill="#f1e6b8"/><text x="142" y="103.5">July</text><rect x="151" y="102" width="1.5" height="1.5" fill="#66379b"/><text x="153" y="103.5">August</text></g>
  </svg>
  <div class="foot"><span>Human Resources services &amp; business coaching.</span><span>BrightPath | 31</span></div>
</section>

<!-- 32 rings -->
<section class="slide">
  <div class="brand">BrightPath</div>
  <h2 class="hd" style="top:8px;left:17px">DATA <b>OVERVIEW</b></h2>
  <div style="left:17px;top:21px;width:178px"><p class="sub" style="margin:0">Subtitle</p><p class="copy" style="color:var(--ink)">Lorem ipsum is simply dummy text of the printing and typesetting industry. Lorem ipsum has been the industry's standard dummy text of simply dummy text of the printing and typesetting industry. Lorem ipsum has been the industry's standard dummy text ever since the printing and typesetting industry began.</p></div>
  <svg style="left:0;top:0" width="210" height="118" viewBox="0 0 210 118">
    <g fill="none" stroke="#e8e8ec" stroke-width="2.4"><circle cx="40" cy="60" r="9"/><circle cx="84" cy="60" r="9"/><circle cx="128" cy="60" r="9"/><circle cx="172" cy="60" r="9"/></g>
    <g fill="none" stroke-width="2.4" stroke-linecap="round">
      <circle cx="40" cy="60" r="9" pathLength="100" stroke="#17a196" stroke-dasharray="10 90" transform="rotate(-90 40 60)"/>
      <circle cx="84" cy="60" r="9" pathLength="100" stroke="#f5a623" stroke-dasharray="35 65" transform="rotate(-90 84 60)"/>
      <circle cx="128" cy="60" r="9" pathLength="100" stroke="#ef5a7a" stroke-dasharray="15 85" transform="rotate(-90 128 60)"/>
      <circle cx="172" cy="60" r="9" pathLength="100" stroke="#17a196" stroke-dasharray="50 50" transform="rotate(-90 172 60)"/>
    </g>
    <g font-size="4" font-weight="700" text-anchor="middle" fill="#2b2b33"><text x="40" y="61.5">10%</text><text x="84" y="61.5">35%</text><text x="128" y="61.5">15%</text><text x="172" y="61.5">50%</text></g>
  </svg>
  <p class="lbl" style="left:28px;top:81px;width:26px;text-align:left"><strong>Data title here</strong>A peep at some distant orb has power to raise and purify.</p>
  <p class="lbl" style="left:72px;top:81px;width:26px;text-align:left"><strong>Data title here</strong>A peep at some distant orb has power to raise and purify.</p>
  <p class="lbl" style="left:116px;top:81px;width:26px;text-align:left"><strong>Data title here</strong>A peep at some distant orb has power to raise and purify.</p>
  <p class="lbl" style="left:160px;top:81px;width:26px;text-align:left"><strong>Data title here</strong>A peep at some distant orb has power to raise and purify.</p>
  <div class="foot"><span>Human Resources services &amp; business coaching.</span><span>BrightPath | 32</span></div>
</section>

<!-- 33 core services concentric -->
<section class="slide">
  <div class="brand">BrightPath</div>
  <h2 class="hd" style="top:8px;left:17px">OUR <b>CORE SERVICES</b></h2>
  <svg style="left:0;top:0" width="210" height="118" viewBox="0 0 210 118">
    <circle cx="58" cy="68" r="42" fill="#f1e6b8"/>
    <circle cx="58" cy="75" r="35" fill="#17a196"/>
    <circle cx="58" cy="82" r="28" fill="#ef5a7a"/>
    <circle cx="58" cy="89" r="21" fill="#f5a623"/>
    <circle cx="58" cy="96" r="13" fill="#66379b"/>
    <g font-size="3" fill="#fff" text-anchor="middle"><text x="58" y="32">Maintenance</text><text x="58" y="45">Marketing</text><text x="58" y="58">Web design</text><text x="58" y="72">UI/UX</text><text x="58" y="94">Marketing</text><text x="58" y="98">Services</text></g>
  </svg>
  <div style="left:112px;top:29px;width:82px"><p class="sub" style="margin:0">Subtitle</p><p class="copy" style="color:var(--ink)">Lorem ipsum is simply dummy text of the printing and typesetting industry. Lorem ipsum has been the industry's standard dummy text of simply dummy text of the printing and typesetting industry.</p><p class="copy" style="color:var(--ink)">Lorem ipsum is simply dummy text of the printing and typesetting industry. Lorem ipsum has been the industry's standard dummy text of simply dummy text.</p><p class="copy" style="color:var(--ink)">Lorem ipsum is simply dummy text of the printing and typesetting industry. Lorem ipsum has been the industry's standard dummy text of simply dummy text.</p></div>
  <div class="foot"><span>Human Resources services &amp; business coaching.</span><span>BrightPath | 33</span></div>
</section>

<!-- 34 venn -->
<section class="slide">
  <div class="brand">BrightPath</div>
  <h2 class="hd" style="top:8px;left:17px">OUR <b>CORE SERVICES</b></h2>
  <div style="left:14px;top:29px;width:82px"><p class="sub" style="margin:0">Subtitle</p><p class="copy" style="color:var(--ink)">Lorem ipsum is simply dummy text of the printing and typesetting industry. Lorem ipsum has been the industry's standard dummy text of simply dummy text of the printing and typesetting industry.</p><p class="copy" style="color:var(--ink)">Lorem ipsum is simply dummy text of the printing and typesetting industry. Lorem ipsum has been the industry's standard dummy text of simply dummy text.</p><p class="copy" style="color:var(--ink)">Lorem ipsum is simply dummy text of the printing and typesetting industry. Lorem ipsum has been the industry's standard dummy text of simply dummy text.</p></div>
  <svg style="left:0;top:0" width="210" height="118" viewBox="0 0 210 118">
    <g opacity=".88">
      <circle cx="148" cy="44" r="15" fill="#ef5a7a"/>
      <circle cx="164" cy="61" r="15" fill="#f5a623"/>
      <circle cx="132" cy="61" r="15" fill="#66379b"/>
      <circle cx="148" cy="79" r="15" fill="#17a196"/>
    </g>
    <g font-size="3" fill="#fff" text-anchor="middle"><text x="148" y="40">Marketing</text><text x="169" y="60">Creative</text><text x="169" y="63.5">Proposal</text><text x="127" y="60">Motion</text><text x="127" y="63.5">Design</text><text x="148" y="84">Human</text><text x="148" y="87.5">resources</text></g>
  </svg>
  <div class="foot"><span>Human Resources services &amp; business coaching.</span><span>BrightPath | 34</span></div>
</section>

<!-- 35 table -->
<section class="slide">
  <div class="brand">BrightPath</div>
  <h2 class="hd" style="top:8px;left:17px">TABLE <b>DESIGN</b></h2>
  <table style="left:25px;top:31px;width:160px">
    <tr><th></th><th>Column Title</th><th>Column Title</th><th>Column Title</th><th>Column Title</th></tr>
    <tr><td>First Row</td><td>120151</td><td>583101</td><td>234858</td><td>132771</td></tr>
    <tr><td>Second Row</td><td>128078289</td><td>838459</td><td>4099</td><td>737910</td></tr>
    <tr><td>Third Row</td><td>48649</td><td>848908</td><td>71617</td><td>65881</td></tr>
    <tr><td>Rowname</td><td>8973897</td><td>32455467</td><td>6547</td><td>789879</td></tr>
    <tr><td>Below</td><td>1201511</td><td>583101</td><td>234858</td><td>132771</td></tr>
    <tr><td>Rowname</td><td>128078289</td><td>838459</td><td>4099</td><td>737910</td></tr>
    <tr><td>Last Row</td><td>128078289</td><td>838459</td><td>4099</td><td>737910</td></tr>
    <tr><td>Total</td><td>1.000.000$</td><td>2.300.000$</td><td>3.400.000$</td><td>92.400.000$</td></tr>
  </table>
  <div class="foot"><span>Human Resources services &amp; business coaching.</span><span>BrightPath | 35</span></div>
</section>

<!-- 36 table -->
<section class="slide">
  <div class="brand">BrightPath</div>
  <h2 class="hd" style="top:8px;left:17px">TABLE <b>DESIGN</b></h2>
  <table style="left:25px;top:27px;width:165px">
    <tr><th style="background:none"></th><th>Option 1</th><th>Column Title</th><th>Column Title</th><th>Column Title</th><th>Column Title</th></tr>
    <tr><td>First Row</td><td>120151</td><td>583101</td><td>234858</td><td>132771</td><td>229846</td></tr>
    <tr><td>Second Row</td><td>128078289</td><td>838459</td><td>4099</td><td>737910</td><td>864123</td></tr>
    <tr><td>Third Row</td><td>48649</td><td>848908</td><td>71617</td><td>65881</td><td>95014</td></tr>
    <tr><td>Rowname</td><td>8973897</td><td>32455467</td><td>6547</td><td>789879</td><td>235478</td></tr>
    <tr><td>Below</td><td>1201511</td><td>583101</td><td>234858</td><td>132771</td><td>152368</td></tr>
    <tr><td>Rowname</td><td>128078289</td><td>838459</td><td>4099</td><td>737910</td><td>31485</td></tr>
    <tr><td style="font-weight:700;color:var(--ink)">Total</td><td><b>1.000.000$</b></td><td><b>2.300.000$</b></td><td><b>3.400.000$</b></td><td><b>92.400.000$</b></td><td><b>99.900.000$</b></td></tr>
  </table>
  <div class="foot"><span>Human Resources services &amp; business coaching.</span><span>BrightPath | 36</span></div>
</section>

</main>
</body>
</html>
```